Looking for an attractive, cool poster design for our company Core Values. This would ideally be framed and placed at each company location. Would like this to be striking and memorable.

The core values that should be included on the poster are:

Be a Creator
Have an Open Mind
Do the Right Thing

The size should be standard poster size, 18 x 24, vertical orientation ideally.

The company name to include on the poster is:

Brightwater Systems Group

The design could be printed as a poster or a sticker/decal as well. Or perhaps printed on a fabric, foam boards. Versatile enough design for different output types.

Target Market(s)

Internal Team Members and visitors

Industry/Entity Type

Technology

Font styles to use
Other font styles liked:
• Montserrat

Requirements
Must have
• The design could be printed as a poster or a sticker/decal as well. Or perhaps printed on a fabric. Versatile enough design for different output types.

```html
<!DOCTYPE html>
<html lang="en">
<head>
<meta charset="utf-8">
<title>Core Values – Brightwater Systems Group</title>
<link rel="stylesheet" href="https://fonts.googleapis.com/css2?family=Bebas+Neue&family=Kaushan+Script&family=Londrina+Solid:wght@900&family=Montserrat:wght@800;900&display=swap">
<style>
  :root {
    --navy: #05446b;
    --orange: #e68a25;
    --orange-deep: #d06f16;
    --orange-fold: #a64a00;
    --white: #ffffff;
  }
  html, body {
    margin: 0;
    padding: 0;
    width: 800px;
    height: 1200px;
    overflow: hidden;
    background: var(--navy);
  }
  .poster {
    display: block;
    width: 800px;
    height: 1200px;
  }
  .poster__bg { fill: var(--navy); }
  .ribbon__face { fill: var(--orange); }
  .ribbon__tail { fill: var(--orange-deep); }
  .ribbon__fold { fill: var(--orange-fold); }
  .rule { fill: var(--orange); }
  .ribbon__label {
    font-family: "Montserrat", sans-serif;
    font-weight: 900;
    fill: var(--white);
  }
  .value--creator {
    font-family: "Bebas Neue", sans-serif;
    fill: var(--white);
  }
  .value--mind {
    font-family: "Kaushan Script", cursive;
    fill: var(--orange);
  }
  .value--right {
    font-family: "Montserrat", sans-serif;
    font-weight: 900;
    fill: var(--white);
  }
  .value--think {
    font-family: "Londrina Solid", sans-serif;
    font-weight: 900;
    fill: var(--white);
  }
  .brand__dot { fill: var(--orange); }
  .brand__name {
    font-family: "Montserrat", sans-serif;
    font-weight: 900;
    fill: var(--white);
  }
</style>
</head>
<body>
<svg class="poster" viewBox="0 0 800 1200" xmlns="http://www.w3.org/2000/svg" role="img" aria-label="Core values poster for Brightwater Systems Group">
  <rect class="poster__bg" width="800" height="1200"/>

  <g class="ribbon">
    <polygon class="ribbon__tail" points="42,82 143,82 143,175 42,175 84,128"/>
    <polygon class="ribbon__tail" points="758,82 657,82 657,175 758,175 716,128"/>
    <polygon class="ribbon__fold" points="114,157 143,157 143,175"/>
    <polygon class="ribbon__fold" points="686,157 657,157 657,175"/>
    <rect class="ribbon__face" x="114" y="63" width="571" height="94"/>
    <text class="ribbon__label" x="400" y="136" text-anchor="middle" font-size="76" textLength="516" lengthAdjust="spacingAndGlyphs">CORE VALUES</text>
  </g>

  <text class="value value--creator" x="47" y="369" font-size="196" textLength="703" lengthAdjust="spacingAndGlyphs">BE A CREATOR</text>

  <rect class="rule" x="0" y="405" width="800" height="10"/>

  <g class="value value--mind">
    <text x="410" y="515" text-anchor="middle" font-size="86" textLength="300" lengthAdjust="spacingAndGlyphs">Have an</text>
    <text x="42" y="655" font-size="170" textLength="713" lengthAdjust="spacingAndGlyphs">Open Mind</text>
  </g>

  <rect class="rule" x="0" y="695" width="800" height="11"/>

  <text class="value value--right" x="151" y="803" font-size="69" textLength="501" lengthAdjust="spacingAndGlyphs">DO THE RIGHT</text>
  <text class="value value--think" x="151" y="1027" font-size="268" textLength="490" lengthAdjust="spacingAndGlyphs">THINK</text>

  <g class="brand">
    <rect class="rule" x="0" y="1117" width="127" height="11"/>
    <rect class="rule" x="673" y="1117" width="127" height="11"/>
    <circle class="brand__dot" cx="195" cy="1122" r="30"/>
    <text class="brand__name" x="248" y="1116" font-size="40" textLength="390" lengthAdjust="spacingAndGlyphs">BRIGHTWATER</text>
    <text class="brand__name" x="248" y="1148" font-size="26" textLength="390" lengthAdjust="spacingAndGlyphs">SYSTEMS GROUP</text>
  </g>
</svg>
</body>
</html>
```